Business Card Design Project

colors are orange and blue (marlow crest university football orange and blue.

need jpeg to build a business card
fill 2/3 of biz card on top half of card

I need a orange swoosh (looks like a line painted by a paintbrush used on outside of the house) the orange line should trail off at the end.
underscore the orange swoosh with a blue shelf.make the left side of the shelf ornamental like it fits into the corner of the wall

Target Market(s)

life coach business consultant. orange means enthusiasm and blue is stability and competence

Industry/Entity Type

University

Requirements
Must have
• add very simple paint example. orange must be marlow crest u football color orange and same w/ the blue. orange is to be like a wide paint brush. blue below will look like a shelf w/ an edge that fits into a corner wall.

```html
<!DOCTYPE html>
<html lang="en">
<head>
<meta charset="utf-8">
<title>Marlow Crest University – Card Swoosh</title>
<style>
  :root {
    --card-bg: #ffffff;
    --paint-orange: #f5821f;
    --paint-orange-light: #f8a850;
    --shelf-blue-dark: #3a76a4;
    --shelf-blue-mid: #3aa2cc;
    --shelf-blue-light: #48d0ef;
  }
  html, body {
    margin: 0;
    padding: 0;
    width: 1200px;
    height: 864px;
    overflow: hidden;
    background: var(--card-bg);
  }
  .card {
    position: relative;
    width: 1200px;
    height: 864px;
    background: var(--card-bg);
  }
  .card__art {
    position: absolute;
    inset: 0;
    width: 1200px;
    height: 864px;
    display: block;
  }
  .paint-stop--deep { stop-color: var(--paint-orange); }
  .paint-stop--soft { stop-color: var(--paint-orange-light); }
  .shelf-stop--dark { stop-color: var(--shelf-blue-dark); }
  .shelf-stop--mid { stop-color: var(--shelf-blue-mid); }
  .shelf-stop--light { stop-color: var(--shelf-blue-light); }
</style>
</head>
<body>
  <main class="card">
    <svg class="card__art" viewBox="0 0 624 450" preserveAspectRatio="none" aria-hidden="true">
      <defs>
        <linearGradient id="brush-stroke-fill" x1="0" y1="0" x2="600" y2="0" gradientUnits="userSpaceOnUse">
          <stop offset="0" class="paint-stop--soft" stop-opacity="0.85"/>
          <stop offset="0.25" class="paint-stop--deep" stop-opacity="0.85"/>
          <stop offset="0.5" class="paint-stop--deep" stop-opacity="0.95"/>
          <stop offset="0.72" class="paint-stop--soft" stop-opacity="0.8"/>
          <stop offset="0.86" class="paint-stop--soft" stop-opacity="0.35"/>
          <stop offset="0.97" class="paint-stop--soft" stop-opacity="0"/>
        </linearGradient>
        <linearGradient id="shelf-fill" x1="0" y1="0" x2="615" y2="0" gradientUnits="userSpaceOnUse">
          <stop offset="0" class="shelf-stop--light"/>
          <stop offset="0.3" class="shelf-stop--mid"/>
          <stop offset="0.5" class="shelf-stop--dark"/>
          <stop offset="0.72" class="shelf-stop--mid"/>
          <stop offset="1" class="shelf-stop--light"/>
        </linearGradient>
      </defs>

      <path class="brush-stroke"
            fill="url(#brush-stroke-fill)"
            d="M0,190 C60,206 120,216 190,193 C260,168 320,120 420,100
               C480,89 540,98 585,125 L592,172
               C540,180 470,172 400,186 C330,201 280,240 220,262
               C150,288 80,296 0,284 Z"/>

      <path class="shelf-line"
            fill="url(#shelf-fill)"
            d="M0,289 C60,311 130,318 200,290 C270,260 330,210 420,192
               C500,178 560,200 615,262
               C560,210 500,191 425,199 C340,214 280,266 205,299
               C130,328 60,320 0,296 Z"/>
    </svg>
  </main>
</body>
</html>
```